Brochure, website and corporate stationary Design Project

Project scope:
1 x brochure (A4 insert) design
1 x brochure folder design (both external pages and one internal (there will be a few lines of text on the left inside page). The internal right side page will be a pocket for brochures (A4 inserts)
1 x corporate stationary pack (Business Card, logo (a proper logo file format needs to be produced), Letterhead and Envelope)
1 x concept design for our website. You dont need to do the coding. What you need to deliver is the design in a standard format (i.e. photoshop or blend)
Summary: the scope of the project is to design our brochure and its brochure folder, corporate stationary design and graphics concept design for our website. You should also consider our existing logo when performing the above design work (you can modify the logo slightly if you think it would improve look and feel and relevancy to overall design).
• We are a small IT services company
• The folder will be used to hold the brochures (inserts). The folder will be given to prospect customers (see attached a sample service brochure called “Fjällux User support services Ver0.1.docx”)
• On the cover of the folder, we want to have a design that uses keywords / phrases that reflects our main services (see attached file called “Phrases for presentation folder.docs”). Please note that not all phrases have to be used, use a logic in which ones or add new suggestions
• Inside the folder, at left side we want to have a short text explaining about our services a bit (see attached file called “Brochure Main section v0.91.docx”)
• All designs (corporate stationary, brochure, folder, web, etc.) must be consistent with each other and follow same concept, colour scheme, etc
• you are allowed to do minor changes to our existing logo if you have good reason to do so (see attached logo)
• We want our website design to be simple, elegant, not very colourful, light. HTML5. No flash. (you dont need to do the actual coding of the website, just deliver the design in Photoshop, Blend or any other standard format) With minimal menu items such as: home, services, about us, news, contact us, and other important ones if any. Same colour and design scheme as corporate stationary and brochures
• The company name “Fjällux” is derived from the Swedish word “Grön” (meaning green) and “teQ” which stands for technology but spelled with a “Q” to resemble Quality. The corporate green colour comes from the word “Grön”.
• All templates must be delivered in a standard editable format
Reason: To provide more time to the designers to come with their design submissions.
please note that we more than doubled the budget for this project
We deliver IT services to companies of 3-4 employees upto 200-300 employees. The brochures are intended for prospect customers (non IT people)
Business

```html
<!DOCTYPE html>
<html lang="en">
<head>
<meta charset="utf-8">
<title>Fjällux Stationery</title>
<link href="https://fonts.googleapis.com/css2?family=Rajdhani:wght@600;700&display=swap" rel="stylesheet">
<style>
  :root {
    --backdrop: #ebebeb;
    --paper: #ffffff;
    --ink: #1c1c1c;
    --brand-green: #6fba3f;
    --brand-green-dark: #4b7f2b;
    --brand-green-mid: #5a9a33;
    --shadow: 3px 5px 9px rgba(0,0,0,0.28);
  }
  html, body {
    margin: 0; padding: 0;
    width: 1200px; height: 800px;
    overflow: hidden;
    background: var(--backdrop);
    font-family: "Rajdhani", "Arial Narrow", sans-serif;
  }
  .stage { position: relative; width: 1200px; height: 800px; }
  .sheet { position: absolute; background: var(--paper); box-shadow: var(--shadow); }
  .wordmark {
    position: absolute; margin: 0;
    font-weight: 700; color: var(--ink);
    letter-spacing: 0.5px; line-height: 1;
  }
  .small-copy {
    position: absolute; margin: 0;
    font-weight: 700; color: var(--ink);
    text-transform: uppercase; line-height: 1.3;
  }
  .web-line { position: absolute; display: flex; align-items: center; }
  .web-line .url { font-weight: 700; color: var(--brand-green); text-transform: uppercase; }
  .web-line .bar { background: var(--brand-green); border-radius: 2px; }

  /* Letterhead */
  .letterhead { left: 63px; top: 67px; width: 513px; height: 667px; }
  .letterhead .wordmark { left: 40px; top: 37px; font-size: 25px; }
  .letterhead .small-copy { left: 39px; top: 577px; font-size: 8.6px; line-height: 10.3px; }
  .letterhead .web-line { left: 39px; top: 627px; width: 426px; gap: 12px; }
  .letterhead .url { font-size: 9px; }
  .letterhead .bar { flex: 1; height: 6px; }

  /* Envelope back */
  .envelope-back { left: 560px; top: 408px; width: 550px; height: 240px; }
  .envelope-back .flap { position: absolute; left: 0; top: 0; width: 550px; height: 76px; }
  .envelope-back .flap-url {
    position: absolute; left: 244px; top: 44px; margin: 0;
    font-size: 11px; font-weight: 700; color: var(--paper); letter-spacing: 0.3px;
  }

  /* Envelope front */
  .envelope-front { left: 220px; top: 364px; width: 557px; height: 241px; }
  .envelope-front .wordmark { left: 24px; top: 20px; font-size: 23px; }
  .envelope-front .small-copy { left: 23px; top: 48px; font-size: 7.6px; line-height: 9.6px; }

  /* Business cards */
  .card-contact { left: 778px; top: 170px; width: 235px; height: 132px; }
  .card-contact .person { position: absolute; left: 23px; top: 18px; margin: 0; line-height: 1.2; }
  .card-contact .person-name { display: block; font-size: 10px; font-weight: 700; color: var(--ink); text-transform: uppercase; }
  .card-contact .person-role { display: block; font-size: 8.5px; font-weight: 600; color: var(--ink); }
  .card-contact .small-copy { left: 23px; top: 53px; font-size: 8.2px; line-height: 11px; }
  .card-contact .web-line { left: 23px; top: 111px; width: 188px; gap: 10px; }
  .card-contact .url { font-size: 9px; }
  .card-contact .bar { flex: 1; height: 6px; }

  .card-brand { position: absolute; width: 242px; height: 130px; }
  .card-brand.layer-back { left: 874px; top: 77px; background: var(--brand-green-dark); box-shadow: var(--shadow); }
  .card-brand.layer-mid { left: 877px; top: 72px; background: var(--brand-green-mid); }
  .card-brand.layer-front { left: 880px; top: 67px; background: var(--brand-green); }
  .card-brand .wordmark {
    left: 0; right: 0; top: 51px; text-align: center;
    font-size: 24px; color: var(--paper);
  }
</style>
</head>
<body>
<main class="stage">

  <section class="sheet letterhead" aria-label="Letterhead">
    <p class="wordmark">Fjällux</p>
    <p class="small-copy">Building 9, 3rd Floor<br>Northgate Business Park, Dubai, U.A.E.<br>Tel +971 50 234 5678<br>Fax +971 4 555 0192</p>
    <div class="web-line"><span class="url">fjallux.com</span><span class="bar"></span></div>
  </section>

  <section class="sheet envelope-back" aria-label="Envelope back">
    <svg class="flap" viewBox="0 0 550 76" aria-hidden="true">
      <path d="M0 0 H550 Q543 6 544 20 L546 58 Q546 75 530 75 H0 Z" fill="var(--brand-green)"/>
    </svg>
    <p class="flap-url">FJALLUX.COM</p>
  </section>

  <section class="sheet envelope-front" aria-label="Envelope front">
    <p class="wordmark">Fjällux</p>
    <p class="small-copy">Building 9, 3rd Floor<br>Northgate Business Park, Dubai, U.A.E.</p>
  </section>

  <section class="sheet card-contact" aria-label="Business card front">
    <p class="person"><span class="person-name">Erik Lindqvist</span><span class="person-role">CEO</span></p>
    <p class="small-copy">Building 9, 3rd Floor<br>Northgate Business Park, Dubai, U.A.E.<br>Tel +971 50 234 5678<br>Fax +971 4 555 0192</p>
    <div class="web-line"><span class="url">fjallux.com</span><span class="bar"></span></div>
  </section>

  <div class="card-brand layer-back" aria-hidden="true"></div>
  <div class="card-brand layer-mid" aria-hidden="true"></div>
  <section class="card-brand layer-front" aria-label="Business card back">
    <p class="wordmark">Fjällux</p>
  </section>

</main>
</body>
</html>
```